4D Hush Little Nest Luxury Ultrasound Billboard

Design a HIGH-END, MODERN billboard for my private prenatal ultrasound studio, 4D Hush Little Nest, located in Pace, Florida.
This billboard will be viewed by drivers traveling at highway speeds, so it must be extremely clean, simple, and readable within 6 seconds.
About My Business
4D Hush Little Nest is a private prenatal ultrasound studio specializing in:
Highest technology 4D/HD Ultrasounds
Early Gender Determination
Pregnancy Confirmation
I have been serving families for nearly 10 years and is known for creating a memorable experience, not just an ultrasound appointment.
Design Style
I DO NOT want:
Flowers
Leaves
Swirls
Glitter
Hearts everywhere
Busy backgrounds
Generic maternity stock graphics
I DO want:
Modern
Luxury
Upscale
Clean
Professional
Eye-catching
Premium medical spa feel
Colors
Use colors from my logo:
LOGO Green ( or a deep green)
Black
White
Soft Gold accents
Images:
Incorporate my professional headshot in a clean, modern way, logo, and the ultrasound images
Text
Keep wording minimal.
Primary Headline ( OPEN TO IDEAS) :
EXAMPLES ( WOULD RATHER SOMETHING MORE CATCHY)
" ADVANCED IMAGING. UNFORGETTABLE MOMENTS"
"MEET YOUR BABY BEFORE BIRTH"
Under headline:
4D Ultrasound • Early Gender • Pregnancy Confirmation
Business Name:
4D Hush Little Nest
Private Prenatal Ultrasound Studio
Phone Number:
850-471-3905
Important
This billboard must be readable in 5–6 seconds from a moving vehicle.
Less text is better.
The phone number and business name must be visible from a distance.
The design should feel like a premium brand that immediately tells expecting parents:
“This is where I go to see my baby.”
Files Provided
Official logo
Headshot
Ultrasound images
Don’t make this look like a medical office billboard.
Make it look like a luxury baby experience billboard. That’s what separates 4D Hush Little Nest from hospitals, OB offices, and all the new studios popping up around you. The emotional connection is what gets moms to book. ❤️
Billboard Size - 10.6” x 36”

```html
<!DOCTYPE html>
<html lang="en">
<head>
<meta charset="utf-8">
<title>4D Hush Little Nest Billboard</title>
<link href="https://fonts.googleapis.com/css2?family=Oswald:wght@400;500;600;700&family=Montserrat:wght@500;600&display=swap" rel="stylesheet">
<style>
  :root {
    --green: #3b4a38;
    --green-deep: #465544;
    --gold: #c69a23;
    --gold-band: #c2962a;
    --white: #ffffff;
    --paper: #f7f6f2;
    --stage: #e9e8e4;
  }
  * { margin: 0; padding: 0; box-sizing: border-box; }
  html, body { width: 1200px; height: 718px; overflow: hidden; }
  body {
    background: var(--stage);
    font-family: "Oswald", "Arial Narrow", sans-serif;
    position: relative;
  }
  .billboard {
    position: absolute;
    left: 20px; top: 188px;
    width: 1160px; height: 342px;
    background: radial-gradient(ellipse at 40% 0%, var(--white) 0%, var(--paper) 70%);
    overflow: hidden;
    box-shadow: 0 6px 18px rgba(0,0,0,.12);
  }
  .headline {
    position: absolute;
    left: 46px; top: 100px;
    font-weight: 600;
    text-transform: uppercase;
    line-height: 1.0;
    letter-spacing: .3px;
  }
  .headline span { display: block; white-space: nowrap; }
  .headline .line-1 { color: var(--green); font-size: 50px; }
  .headline .line-2 { color: var(--gold); font-size: 41px; margin-top: 4px; }
  .headline .line-3 { color: var(--green); font-size: 41px; margin-top: 2px; }
  .service-band {
    position: absolute;
    left: 0; top: 254px;
    width: 354px; height: 30px;
    background: var(--gold-band);
    color: var(--paper);
    font-size: 12.5px;
    font-weight: 500;
    display: flex; align-items: center;
    padding-left: 46px;
    letter-spacing: .2px;
    white-space: nowrap;
  }
  .headshot {
    position: absolute;
    left: 360px; top: 52px;
    width: 214px; height: 290px;
    border-radius: 90px 90px 0 0;
    background: linear-gradient(180deg, #d9b56e 0%, #c99c62 35%, #3f5a3e 60%, #2f452f 100%);
  }
  .logo-box {
    position: absolute;
    left: 614px; top: 80px;
    width: 208px; height: 100px;
    border: 2px solid var(--green);
    border-radius: 12px;
    background: var(--white);
    display: flex; flex-direction: column;
    align-items: center; justify-content: center;
    gap: 10px;
    text-align: center;
  }
  .logo-name {
    font-weight: 600;
    font-size: 23px;
    color: var(--gold);
    line-height: 1.05;
    white-space: nowrap;
  }
  .logo-tagline {
    font-family: "Montserrat", Arial, sans-serif;
    font-weight: 600;
    font-size: 8px;
    color: var(--green);
    letter-spacing: .3px;
    text-transform: uppercase;
  }
  .phone {
    position: absolute;
    left: 596px; top: 230px;
    display: flex; align-items: center; gap: 6px;
    color: var(--green);
    font-size: 36px;
    font-weight: 600;
    letter-spacing: .3px;
    white-space: nowrap;
  }
  .phone-icon { width: 22px; height: 34px; }
  .side-panel {
    position: absolute;
    left: 780px; top: 0;
    width: 380px; height: 342px;
  }
  .scan-image {
    position: absolute;
    left: 934px; top: 142px;
    width: 190px; height: 158px;
    background: radial-gradient(ellipse at 55% 45%, #c97a64 0%, #a8573f 45%, #5a2516 100%);
  }
</style>
</head>
<body>
  <section class="billboard">
    <h1 class="headline">
      <span class="line-1">Your Baby’s</span>
      <span class="line-2">First Moments,</span>
      <span class="line-3">Unforgettable</span>
    </h1>

    <p class="service-band">4D Ultrasound • Early Gender • Pregnancy Confirmation</p>

    <div class="headshot" role="img" aria-label="Professional headshot of the studio owner in green scrubs holding an ultrasound probe"></div>

    <div class="logo-box">
      <span class="logo-name">4D Hush Little Nest</span>
      <span class="logo-tagline">Prenatal Ultrasound Studio</span>
    </div>

    <div class="phone">
      <svg class="phone-icon" viewBox="0 0 26 40" aria-hidden="true">
        <path d="M8 2 L13 2 L15 11 L11 14 Q11 22 15 28 L19 26 L24 34 L20 38 Q12 40 7 28 Q2 16 4 6 Z" fill="var(--gold)"/>
      </svg>
      <span>850-471-3905</span>
    </div>

    <svg class="side-panel" viewBox="0 0 380 342" preserveAspectRatio="none" aria-hidden="true">
      <path d="M122 0 C98 70 48 120 60 175 C70 230 98 250 90 282 C84 310 36 320 16 342 L380 342 L380 0 Z" fill="var(--gold)"/>
      <path d="M130 0 C106 70 56 120 68 175 C78 230 106 250 98 282 C92 310 46 320 27 342 L380 342 L380 0 Z" fill="var(--green-deep)"/>
    </svg>

    <div class="scan-image" role="img" aria-label="4D ultrasound image of a baby’s face"></div>
  </section>
</body>
</html>
```